I need to design a business card
on the front side the words "VELTRIS CAPITAL" with the top half surrounded by a stylised cloud. Minimalist, navy blue font on white background, with the Veltris capital in embossing.

On the back contact details (avoid centered). I would rather have the details taking the 2/3rd on the right and having the logo on the left, but anyway not plain centered

Marcello Lo Ruffo
CEO e Fondatore

m.loruffo@veltris-capital.example
+39.328.514.6082

Piazza Ventrano 7
20135 Milano

```html
<!DOCTYPE html>
<html lang="it">
<head>
<meta charset="utf-8">
<title>Veltris Capital – Business Card</title>
<link rel="stylesheet" href="https://fonts.googleapis.com/css2?family=Cinzel:wght@600&family=Montserrat:wght@400&display=swap">
<style>
  :root {
    --backdrop: #e3e3e3;
    --card: #f6f6f6;
    --navy: #1b2541;
    --ink: #3a3a3c;
    --mark-soft: #cfd2da;
    --mark-emboss: #dcdcdc;
    --serif: "Cinzel", "Times New Roman", serif;
    --sans: "Montserrat", Arial, sans-serif;
  }
  * { margin: 0; padding: 0; box-sizing: border-box; }
  html, body {
    width: 1200px; height: 1124px; overflow: hidden;
    background: var(--backdrop);
  }
  .canvas { position: relative; width: 1200px; height: 1124px; }
  .card {
    position: absolute; left: 252px; width: 696px; height: 398px;
    background: var(--card); border-radius: 26px; overflow: hidden;
  }
  .card--contact { top: 134px; }
  .card--brand { top: 592px; }
  .wordmark { position: absolute; left: 0; top: 0; }
  .wordmark text { font-family: var(--serif); font-weight: 600; fill: var(--navy); }
  .mark-area--soft { fill: var(--mark-soft); }
  .mark-area--emboss { fill: var(--mark-emboss); }

  .contact {
    position: absolute; left: 375px; top: 201px; width: 300px;
    font-family: var(--sans); color: var(--ink);
  }
  .contact__name {
    font-family: var(--serif); font-weight: 600; color: var(--navy);
    font-size: 22px; line-height: 26px; letter-spacing: 0;
  }
  .contact__role { font-size: 15.5px; line-height: 20px; }
  .contact__rule { height: 1px; background: var(--navy); margin: 11px 0 10px; width: 283px; }
  .contact__address { font-size: 15.5px; line-height: 20px; }
  .contact__lines { margin-top: 10px; font-size: 15.5px; line-height: 22px; }
  .contact__line { display: flex; align-items: center; gap: 6px; white-space: nowrap; }
  .contact__icon { width: 11px; height: 11px; flex: none; }
</style>
</head>
<body>
<div class="canvas">

  <section class="card card--contact">
    <svg class="wordmark" width="696" height="398">
      <circle class="mark-area--soft" cx="149" cy="68" r="20" role="img" aria-label="Brand mark area above the company name"/>
      <g aria-label="Veltris Capital">
        <text x="149" y="128" font-size="38" text-anchor="middle" textLength="212" lengthAdjust="spacing">VELTRIS</text>
        <text x="149" y="153" font-size="18" text-anchor="middle" textLength="110" lengthAdjust="spacing">CAPITAL</text>
      </g>
    </svg>

    <div class="contact">
      <div class="contact__name">MARCELLO LO RUFFO</div>
      <div class="contact__role">CEO e Fondatore</div>
      <div class="contact__rule"></div>
      <div class="contact__address">Piazza Ventrano 7<br>20135 Milano</div>
      <div class="contact__lines">
        <div class="contact__line">
          <svg class="contact__icon" viewBox="0 0 24 24" aria-hidden="true"><path fill="#1b2541" d="M6.6 10.8a15.1 15.1 0 0 0 6.6 6.6l2.2-2.2c.3-.3.7-.4 1-.2 1.1.4 2.3.6 3.6.6.6 0 1 .4 1 1V20c0 .6-.4 1-1 1A17 17 0 0 1 3 4c0-.6.4-1 1-1h3.5c.6 0 1 .4 1 1 0 1.3.2 2.5.6 3.6.1.3 0 .7-.2 1z"/></svg>
          <span>+39.328.514.6082</span>
        </div>
        <div class="contact__line">
          <svg class="contact__icon" viewBox="0 0 24 24" aria-hidden="true"><path fill="#1b2541" d="M2 9l10-7 10 7v12H2z"/><path fill="#f6f6f6" d="M4 10l8 5 8-5v1l-8 5-8-5z"/></svg>
          <span>m.loruffo@veltris-capital.example</span>
        </div>
      </div>
    </div>
  </section>

  <section class="card card--brand">
    <svg class="wordmark" width="696" height="398">
      <circle class="mark-area--emboss" cx="348" cy="148" r="32" role="img" aria-label="Embossed brand mark area above the company name"/>
      <g aria-label="Veltris Capital">
        <text x="348" y="247" font-size="64" text-anchor="middle" textLength="344" lengthAdjust="spacing">VELTRIS</text>
        <text x="348" y="288" font-size="31" text-anchor="middle" textLength="176" lengthAdjust="spacing">CAPITAL</text>
      </g>
    </svg>
  </section>

</div>
</body>
</html>
```